Updated front page of Brochure Design

We need to upgrade the front page of our brochure to include all that we offer our clients and I would like this expressed visually. Basically people think that we just supply packaging machinery, and we do a lot more than that. The services that we offer that need to be represented on the cover include (these could be in the form of modern icons as a suggestion): Automated Packaging Equipment – Robotic Solutions – Line Integration – Turnkey Solutions – Facility Design - Service Team – Ongoing Support (these icons have been uploaded for use)

Other wording to be on cover: A holistic approach to your packaging line.

The design needs to be inline with current branding and colours. I have attached our branding identity, current corporate brochure, product brochure for reference and the link to website is www.larvondesk.com (do not contact us outside of this medium as we will not respond)

Examples are attached
Updates

Target Market(s)

Manufacturers of food and beverage, FMCG etc

Industry/Entity Type

Manufacturing

Requirements
Must have
• Logo
• Simple, clever, sophisticated design
• Brand colours

```html
<!DOCTYPE html>
<html lang="en">
<head>
<meta charset="utf-8">
<title>Larvon Desk – Brochure Front Page</title>
<link rel="stylesheet" href="https://fonts.googleapis.com/css2?family=Open+Sans:wght@400;700;800&display=swap">
<style>
  :root {
    --brand-yellow: #f0b323;
    --brand-blue: #1a4a93;
    --tile-grey: #d6d6d6;
    --tile-white: #ffffff;
    --band-black: #000000;
    --text-white: #ffffff;
    --cell-w: 134.714px;
    --cell-h: 124.5px;
  }
  * { margin: 0; padding: 0; box-sizing: border-box; }
  html, body {
    width: 943px;
    height: 1200px;
    overflow: hidden;
    background: #ffffff;
    font-family: "Open Sans", Arial, sans-serif;
  }
  .cover {
    position: relative;
    width: 943px;
    height: 1200px;
  }
  .tile-grid {
    position: absolute;
    left: 0; top: 0;
    width: 943px;
    height: 996px;
    display: grid;
    grid-template-columns: repeat(7, var(--cell-w));
    grid-template-rows: repeat(8, var(--cell-h));
  }
  .tile { display: flex; align-items: center; justify-content: center; }
  .tile--y { background: var(--brand-yellow); }
  .tile--b { background: var(--brand-blue); }
  .tile--w { background: var(--tile-white); }
  .tile--g { background: var(--tile-grey); }
  .tile--k { background: var(--band-black); }
  .brand-area {
    grid-column: 1 / 5;
    grid-row: 1 / 3;
    background: var(--tile-white);
    position: relative;
  }
  .brand-name {
    position: absolute;
    left: 45px;
    top: 86px;
    display: flex;
    align-items: center;
    gap: 16px;
  }
  .brand-mark {
    width: 42px;
    height: 42px;
    background: var(--brand-blue);
  }
  .brand-word {
    font-weight: 800;
    font-size: 44px;
    letter-spacing: 0.5px;
    color: var(--band-black);
    line-height: 1;
  }
  .brand-tagline {
    position: absolute;
    left: 104px;
    top: 138px;
    font-size: 20px;
    color: var(--brand-blue);
    white-space: nowrap;
  }
  .brand-tagline .since { color: var(--brand-yellow); }
  .service-icon { width: 102px; height: 102px; }
  .headline-band {
    position: absolute;
    left: 0; top: 996px;
    width: 943px;
    height: 204px;
    background: var(--band-black);
  }
  .headline {
    position: absolute;
    left: 51px;
    top: 20px;
    font-weight: 700;
    text-transform: uppercase;
    line-height: 1;
  }
  .headline-lead {
    display: block;
    color: var(--brand-yellow);
    font-size: 66px;
    letter-spacing: 2px;
  }
  .headline-rest {
    display: block;
    color: var(--text-white);
    font-size: 36px;
    letter-spacing: 1.5px;
    margin-top: 12px;
    line-height: 1.3;
  }
  .service-list {
    position: absolute;
    left: 575px;
    top: 24px;
    list-style: none;
    font-size: 16px;
    letter-spacing: 0.8px;
    line-height: 21.5px;
  }
  .service-list li { display: flex; align-items: center; gap: 8px; color: var(--text-white); }
  .service-list li.accent { color: var(--brand-yellow); }
  .tick { width: 12px; height: 10px; }
</style>
</head>
<body>
<main class="cover">
  <section class="tile-grid">
    <!-- row 1 & 2 -->
    <div class="brand-area">
      <div class="brand-name"><span class="brand-mark"></span><span class="brand-word">LARVON DESK</span></div>
      <p class="brand-tagline">Engineering Excellence. <span class="since">Since 1926.</span></p>
    </div>
    <div class="tile tile--y"></div>
    <div class="tile tile--b"></div>
    <div class="tile tile--y"></div>
    <div class="tile tile--b">
      <svg class="service-icon" viewBox="0 0 100 100" role="img" aria-label="Automated packaging equipment icon: stacked boxes on a pallet">
        <circle cx="50" cy="50" r="46" fill="none" stroke="#fff" stroke-width="3"/>
      </svg>
    </div>
    <div class="tile tile--w"></div>
    <div class="tile tile--w"></div>
    <!-- row 3 -->
    <div class="tile tile--y"></div>
    <div class="tile tile--b">
      <svg class="service-icon" viewBox="0 0 100 100" role="img" aria-label="Service team icon: two engineers with a checklist">
        <circle cx="50" cy="50" r="46" fill="none" stroke="#fff" stroke-width="3"/>
      </svg>
    </div>
    <div class="tile tile--g"></div>
    <div class="tile tile--b"></div>
    <div class="tile tile--y"></div>
    <div class="tile tile--b"></div>
    <div class="tile tile--y"></div>
    <!-- row 4 -->
    <div class="tile tile--w"></div>
    <div class="tile tile--w"></div>
    <div class="tile tile--b"></div>
    <div class="tile tile--k">
      <svg class="service-icon" viewBox="0 0 100 100" role="img" aria-label="Ongoing support icon: gears with a wrench">
        <circle cx="50" cy="50" r="46" fill="none" stroke="#f0b323" stroke-width="3"/>
      </svg>
    </div>
    <div class="tile tile--g"></div>
    <div class="tile tile--w"></div>
    <div class="tile tile--w"></div>
    <!-- row 5 -->
    <div class="tile tile--b"></div>
    <div class="tile tile--w"></div>
    <div class="tile tile--g"></div>
    <div class="tile tile--w"></div>
    <div class="tile tile--w"></div>
    <div class="tile tile--y"></div>
    <div class="tile tile--b"></div>
    <!-- row 6 -->
    <div class="tile tile--y"></div>
    <div class="tile tile--b"></div>
    <div class="tile tile--w"></div>
    <div class="tile tile--w"></div>
    <div class="tile tile--y"></div>
    <div class="tile tile--b">
      <svg class="service-icon" viewBox="0 0 100 100" role="img" aria-label="Robotic solutions icon: industrial robot arm">
        <circle cx="50" cy="50" r="46" fill="none" stroke="#fff" stroke-width="3"/>
      </svg>
    </div>
    <div class="tile tile--y"></div>
    <!-- row 7 -->
    <div class="tile tile--g"></div>
    <div class="tile tile--y"></div>
    <div class="tile tile--b"></div>
    <div class="tile tile--k">
      <svg class="service-icon" viewBox="0 0 100 100" role="img" aria-label="Turnkey solutions icon: factory with delivery truck">
        <circle cx="50" cy="50" r="46" fill="none" stroke="#f0b323" stroke-width="3"/>
      </svg>
    </div>
    <div class="tile tile--b"></div>
    <div class="tile tile--w"></div>
    <div class="tile tile--w"></div>
    <!-- row 8 -->
    <div class="tile tile--y"></div>
    <div class="tile tile--k">
      <svg class="service-icon" viewBox="0 0 100 100" role="img" aria-label="Line integration icon: two interlocking gears with arrows">
        <circle cx="50" cy="50" r="46" fill="none" stroke="#f0b323" stroke-width="3"/>
      </svg>
    </div>
    <div class="tile tile--w"></div>
    <div class="tile tile--w"></div>
    <div class="tile tile--g"></div>
    <div class="tile tile--b">
      <svg class="service-icon" viewBox="0 0 100 100" role="img" aria-label="Facility design icon: engineer at a computer with layout plans">
        <circle cx="50" cy="50" r="46" fill="none" stroke="#fff" stroke-width="3"/>
      </svg>
    </div>
    <div class="tile tile--y"></div>
  </section>

  <section class="headline-band">
    <h1 class="headline">
      <span class="headline-lead">A Holistic</span>
      <span class="headline-rest">Approach to your<br>packaging line</span>
    </h1>
    <ul class="service-list">
      <li><svg class="tick" viewBox="0 0 12 10"><path d="M1 5l3.5 3.5L11 1" fill="none" stroke="currentColor" stroke-width="1.3"/></svg>Automated Packaging Equipment</li>
      <li class="accent"><svg class="tick" viewBox="0 0 12 10"><path d="M1 5l3.5 3.5L11 1" fill="none" stroke="currentColor" stroke-width="1.3"/></svg>Robotic Solutions</li>
      <li><svg class="tick" viewBox="0 0 12 10"><path d="M1 5l3.5 3.5L11 1" fill="none" stroke="currentColor" stroke-width="1.3"/></svg>Line Integration</li>
      <li class="accent"><svg class="tick" viewBox="0 0 12 10"><path d="M1 5l3.5 3.5L11 1" fill="none" stroke="currentColor" stroke-width="1.3"/></svg>Turnkey Solutions</li>
      <li><svg class="tick" viewBox="0 0 12 10"><path d="M1 5l3.5 3.5L11 1" fill="none" stroke="currentColor" stroke-width="1.3"/></svg>Facility Design</li>
      <li class="accent"><svg class="tick" viewBox="0 0 12 10"><path d="M1 5l3.5 3.5L11 1" fill="none" stroke="currentColor" stroke-width="1.3"/></svg>Service Team</li>
      <li><svg class="tick" viewBox="0 0 12 10"><path d="M1 5l3.5 3.5L11 1" fill="none" stroke="currentColor" stroke-width="1.3"/></svg>Ongoing Support</li>
    </ul>
  </section>
</main>
</body>
</html>
```